Core Values Poster for Technology Business

A core values poster for our office. We don't have much in mind beyond a couple of logos (we have two companies) and then the 4 Core Values we want to present. Mostly, we want this to be simple (easy to take in as a reminder in 5-10 seconds) in a very visually appealing way.

If you can incorporate a high-look-and-feel, great, but not if it over complicates the entire poster/sign.

The core values are:
Relationships Matter
Passion Drives us to Excellence
All About Teamwork
Consistent, Resourceful, Relentless

Our file with both logos together is attached. This is a low-res version. We would provide a high-res version for final production.

Industry/Entity Type

Business

Font styles to use
Serif

Colors
ec1f27
0255a3

Requirements
Nice to have
• This is an update. To be able to incorporate some of our corporate look-and-feel, but not have a black background (as on our kovaline.com stie), please see the Video Conferencing Slick file that I have uploaded. Might be able to use parts of this type of format to tie in (but not use it exactly as-is - since this is a client facing document).

```html
<!DOCTYPE html>
<html lang="en">
<head>
<meta charset="utf-8">
<title>Core Values</title>
<link rel="stylesheet" href="https://fonts.googleapis.com/css2?family=Arvo:wght@400;700&family=Permanent+Marker&display=swap">
<style>
  :root {
    --red: #ec1f27;
    --blue: #0255a3;
    --charcoal: #3a3a3c;
    --ink: #333335;
    --white: #ffffff;
  }
  * { margin: 0; padding: 0; box-sizing: border-box; }
  html, body { width: 1200px; height: 943px; overflow: hidden; }
  body { background: var(--charcoal); font-family: "Arvo", Georgia, serif; }
  .poster { position: relative; width: 1200px; height: 943px; overflow: hidden; background: var(--charcoal); }

  .masthead { position: absolute; left: 0; top: 0; width: 959px; height: 194px; background: var(--charcoal); }
  .masthead-title {
    position: absolute; left: 96px; top: 6px;
    font-family: "Permanent Marker", cursive; font-weight: 400;
    font-size: 150px; line-height: 1; color: var(--white); white-space: nowrap;
  }
  .brand-box {
    position: absolute; left: 961px; top: 0; width: 239px; height: 194px; background: var(--white);
    display: flex; flex-direction: column; align-items: center; justify-content: center; gap: 6px;
  }
  .brand-mark { width: 34px; height: 34px; border-radius: 50%; background: var(--red); }
  .brand-name { font-family: "Arvo", Georgia, serif; font-weight: 400; color: var(--ink); text-align: center; }
  .brand-name.primary { font-size: 24px; line-height: 1; }
  .brand-name.sub { font-size: 10px; letter-spacing: 0.5px; text-transform: uppercase; }
  .brand-name.secondary { font-size: 12px; text-transform: uppercase; margin-top: 6px; }

  .value-row { position: absolute; left: 0; width: 1200px; background: var(--white); overflow: hidden; }
  .row-1 { top: 198px; height: 181px; }
  .row-2 { top: 384px; height: 180px; }
  .row-3 { top: 569px; height: 181px; }
  .row-4 { top: 755px; height: 188px; }

  .color-block { position: absolute; top: 0; height: 100%; }
  .color-block.blue { background: var(--blue); }
  .color-block.red { background: var(--red); }

  .value-number {
    position: absolute; font-family: "Arvo", Georgia, serif; font-weight: 700;
    color: var(--white); line-height: 1; font-size: 250px;
  }
  .slab { font-family: "Arvo", Georgia, serif; font-weight: 400; position: absolute; white-space: nowrap; line-height: 1; }
  .marker { font-family: "Permanent Marker", cursive; font-weight: 400; position: absolute; white-space: nowrap; line-height: 1; }
  .ink { color: var(--ink); }
  .text-red { color: var(--red); }
  .text-blue { color: var(--blue); }
  .text-white { color: var(--white); }
</style>
</head>
<body>
<main class="poster">
  <header class="masthead">
    <h1 class="masthead-title">Core Values</h1>
  </header>
  <aside class="brand-box">
    <span class="brand-mark"></span>
    <span class="brand-name primary">Meridian</span>
    <span class="brand-name sub">Technology Solutions</span>
    <span class="brand-name secondary">Harbor Security Group</span>
  </aside>

  <section class="value-row row-1">
    <div class="color-block blue" style="left:0;width:474px;"></div>
    <span class="value-number" style="left:300px;top:-30px;">1</span>
    <span class="slab ink" style="left:573px;top:24px;font-size:68px;">Relationships</span>
    <span class="marker text-blue" style="left:733px;top:76px;font-size:80px;">Matter</span>
  </section>

  <section class="value-row row-2">
    <div class="color-block red" style="left:474px;width:726px;"></div>
    <span class="slab text-red" style="left:87px;top:22px;font-size:68px;">Passion</span>
    <span class="slab ink" style="left:83px;top:98px;font-size:48px;">drives us to</span>
    <span class="value-number" style="left:530px;top:-28px;">2</span>
    <span class="marker text-white" style="left:728px;top:38px;font-size:88px;">Excellence</span>
  </section>

  <section class="value-row row-3">
    <div class="color-block blue" style="left:721px;width:479px;"></div>
    <span class="marker ink" style="left:82px;top:14px;font-size:84px;">All About</span>
    <span class="slab text-blue" style="left:212px;top:80px;font-size:66px;">Teamwork</span>
    <span class="value-number" style="left:765px;top:-28px;">3</span>
  </section>

  <section class="value-row row-4">
    <div class="color-block red" style="left:0;width:228px;"></div>
    <span class="value-number" style="left:38px;top:-6px;">4</span>
    <span class="slab text-red" style="left:245px;top:18px;font-size:64px;">Consistent, Resourceful,</span>
    <span class="marker ink" style="left:606px;top:90px;font-size:90px;">Relentless</span>
  </section>
</main>
</body>
</html>
```